Buch-/eBook-Cover zum Thema Geldmanagement
Zielgruppe
ich benötige ein Buch-Cover (Vorder- und Rückseite) für das Buch Der Pfad der klaren Vermögensführung. Untertitel ist Innere Ruhe und Wohlstand vereint. Das genaue Format ist im Briefing hinterlegt
Aufgabenstellung
Schön wäre es, wenn das Cover hell gehalten wäre. Es soll hochwertig aussehen. Ich habe zwar eigenes Bild-Material angegeben, es können jedoch auch andere Vorschläge kommen.

```html
<!DOCTYPE html>
<html lang="de">
<head>
<meta charset="utf-8">
<title>Der Pfad der klaren Vermögensführung – Buchcover</title>
<link href="https://fonts.googleapis.com/css2?family=Oswald:wght@500;600&family=Open+Sans:wght@400;600;700&display=swap" rel="stylesheet">
<style>
  :root {
    --page-bg: #e6e6e4;
    --cover-light: #fbfbfb;
    --cover-mid: #eeeeee;
    --cover-shade: #dedfe0;
    --gold: #cfa32f;
    --ink: #1c1c1c;
    --panel: rgba(255,255,255,0.93);
    --art-warm: #e8b65a;
    --art-stone: #f4f3f1;
    --art-sand: #e3e2df;
  }
  * { box-sizing: border-box; margin: 0; padding: 0; }
  html, body { width: 1200px; height: 800px; overflow: hidden; }
  body {
    background: var(--page-bg);
    font-family: "Open Sans", sans-serif;
    color: var(--ink);
    position: relative;
  }
  .cover {
    position: absolute;
    top: 40px;
    width: 480px;
    height: 720px;
    background: radial-gradient(ellipse at 50% 72%, var(--cover-light) 0%, var(--cover-mid) 55%, var(--cover-shade) 100%);
    box-shadow: 0 6px 22px rgba(0,0,0,0.18);
    overflow: hidden;
  }
  .cover--back { left: 90px; }
  .cover--front { left: 630px; text-align: center; }

  /* Front */
  .front-title { margin-top: 56px; padding: 0 40px; }
  .front-title__main {
    font-family: "Oswald", sans-serif;
    font-weight: 600;
    color: var(--gold);
    font-size: 96px;
    line-height: 1;
    letter-spacing: 2px;
  }
  .front-title__mid {
    display: flex;
    align-items: center;
    justify-content: center;
    gap: 12px;
    margin: 8px 0 4px;
    font-size: 22px;
    letter-spacing: 6px;
    font-weight: 400;
  }
  .front-title__mid::before,
  .front-title__mid::after {
    content: "";
    width: 34px;
    height: 2px;
    background: var(--ink);
  }
  .front-title__end {
    font-family: "Oswald", sans-serif;
    font-weight: 600;
    color: var(--gold);
    font-size: 45px;
    line-height: 1.1;
    letter-spacing: 0.5px;
  }
  .front-subtitle {
    margin-top: 12px;
    font-size: 12.5px;
    letter-spacing: 1.6px;
    font-weight: 600;
    text-transform: uppercase;
  }
  .front-art {
    position: absolute;
    left: 20px;
    top: 318px;
    width: 440px;
    height: 330px;
    border-radius: 40px;
    background: radial-gradient(ellipse 60% 55% at 50% 48%, var(--art-warm) 0%, #efd6a4 30%, var(--art-stone) 60%, var(--art-sand) 85%, rgba(238,238,238,0) 100%);
  }
  .author {
    font-size: 18px;
    letter-spacing: 4px;
    font-weight: 400;
  }
  .cover--front .author {
    position: absolute;
    left: 0; right: 0;
    bottom: 36px;
  }

  /* Back */
  .back-panel {
    position: absolute;
    left: 60px;
    top: 90px;
    width: 360px;
    height: 400px;
    background: var(--panel);
    padding: 26px 30px;
  }
  .back-title {
    font-size: 19px;
    font-weight: 700;
    text-align: center;
    letter-spacing: 1px;
    line-height: 1.2;
    text-transform: uppercase;
  }
  .back-blurb {
    margin-top: 30px;
    font-size: 13.5px;
    line-height: 1.5;
    text-align: justify;
    hyphens: auto;
  }
  .cover--back .author {
    position: absolute;
    left: 30px;
    bottom: 26px;
    font-size: 16px;
    letter-spacing: 3px;
  }
  .back-art {
    position: absolute;
    left: 30px;
    top: 510px;
    width: 420px;
    height: 200px;
    border-radius: 36px;
    background: radial-gradient(ellipse 60% 60% at 50% 55%, var(--art-warm) 0%, #efd6a4 32%, var(--art-stone) 62%, var(--art-sand) 85%, rgba(238,238,238,0) 100%);
  }
</style>
</head>
<body>
  <section class="cover cover--back">
    <div class="back-panel">
      <h2 class="back-title">Der Pfad der klaren<br>Vermögensführung</h2>
      <p class="back-blurb">Haben Sie sich schon immer gefragt, was es für ein bewusstes Geldmanagement braucht und wie es Ihnen gelingen kann, in den Zustand von Fülle zu kommen? Wussten Sie, dass es eine Verbindung zwischen Geld und Spiritualität gibt? Möchten Sie wissen, wie Sie in den Geldfluss kommen können und auf welche Art und Weise sich Ihr finanzielles Handeln langfristig zum Positiven verändert? Dann lesen Sie jetzt dieses Buch!</p>
      <p class="author">AUTOR NAME</p>
    </div>
    <div class="back-art" role="img" aria-label="Schmetterling auf Euro-Scheinen und Münzen im hellen Zen-Sand"></div>
  </section>

  <section class="cover cover--front">
    <header class="front-title">
      <h1 class="front-title__main">DER PFAD</h1>
      <p class="front-title__mid">DER KLAREN</p>
      <p class="front-title__end">VERMÖGENSFÜHRUNG</p>
    </header>
    <p class="front-subtitle">- Innere Ruhe und Wohlstand vereint -</p>
    <div class="front-art" role="img" aria-label="Schmetterling auf gestapelten weißen Steinen mit Euro-Scheinen und Münzen in Zen-Sand-Wellen"></div>
    <p class="author">AUTOR NAME</p>
  </section>
</body>
</html>
```